Brivane Communications - veteran and exclusive boutique copywriting agency

PROJECT NEEDS:
1. Website design - full homepage design and inner page top banner design
2. Logo design
* Please see attached Briefs (Word Docs) for descriptions of what is needed for 1 and 2 above.
ABOUT THE CLIENT:
Brivane Communications is a veteran and exclusive boutique copywriting agency run by Martin Olafsky. Martin is an award-winning published novelist and an accomplished executive ghostwriter with articles regularly published prominent technology publications like Pulsar, ByteHarbor, CapitalDrift, and more. For nearly three decades, Martin has focused solely on the technology sector - serving clients in Israel, Europe and the US.

Target Market(s)

hi-tech companies run by serious, confident professionals.

Industry/Entity Type

Business

Number of Pages Required

2 page

Font styles to use
Sans Serif
Other font styles liked:
• font should be modern

Colors
0054AA
0677BA
7BADD7
CADEEF
E8F1F8
F0912C
F2A743
F7CA91
FBE8D2
FDF5EE

Requirements
Must have
• psd files for logo, homepage design, and inner page top banner design
Nice to have
• Please see attached Website and Logo Design Briefs (Word Docs)
Should not have

```html
<!DOCTYPE html>
<html lang="en">
<head>
<meta charset="utf-8">
<title>Brivane Communications</title>
<link href="https://fonts.googleapis.com/css2?family=Poppins:ital,wght@0,400;0,500;0,600;0,700;1,400&display=swap" rel="stylesheet">
<style>
:root{
  --ink:#111111;
  --muted:#555555;
  --royal:#0000a6;
  --bright:#0a0aff;
  --orange:#ffa400;
  --logo-red:#e8532f;
  --hero-bg:#f6f6f6;
  --photo-bg:#efefef;
  --white:#ffffff;
}
*{box-sizing:border-box;margin:0;padding:0}
html,body{width:1200px;height:4135px;overflow:hidden}
body{font-family:'Poppins',sans-serif;color:var(--ink);background:var(--white);position:relative}
.abs{position:absolute}

/* header */
.site-header{position:absolute;left:0;top:0;width:1200px;height:100px;background:var(--white);box-shadow:0 2px 8px rgba(0,0,0,.08);z-index:2}
.brand{position:absolute;left:62px;top:24px;font-size:30px;font-weight:600;color:var(--logo-red);letter-spacing:.5px}
.main-nav{position:absolute;right:70px;top:32px;display:flex;gap:38px;font-size:25px;font-weight:500}

/* hero */
.hero{position:absolute;left:0;top:100px;width:1200px;height:615px;background:var(--hero-bg)}
.hero-photo{position:absolute;left:576px;top:0;width:624px;height:615px;background:linear-gradient(180deg,#f1f1f1,#e6e9ee);border-bottom-left-radius:30px}
.hero-title{position:absolute;left:86px;top:120px;font-size:66px;font-weight:600;line-height:76px}
.hero-sub{position:absolute;left:86px;top:295px;width:440px;font-size:22px;font-style:italic;line-height:28px}
.btn{position:absolute;display:flex;align-items:center;justify-content:center;font-size:15px;font-weight:600;border-radius:4px}
.btn-primary{background:var(--bright);color:var(--white)}
.btn-outline{border:2px solid var(--ink);color:var(--ink)}
.btn-accent{background:var(--orange);color:var(--white)}

/* about */
.about-panel{position:absolute;left:0;top:758px;width:577px;height:594px;background:var(--royal);border-top-right-radius:30px}
.portrait{position:absolute;left:105px;top:845px;width:370px;height:370px;border-radius:50%;background:radial-gradient(circle at 50% 45%,#9fc1e6,#3b5fae 70%,#0a108c)}
.about-title{position:absolute;left:620px;top:815px;font-size:56px;font-weight:600}
.about-text{position:absolute;left:616px;top:910px;width:560px;font-size:19px;font-style:italic;line-height:31.2px;color:#333}

/* why */
.why-title{position:absolute;left:0;top:1400px;width:1200px;text-align:center;font-size:64px;font-weight:700}
.reason{position:absolute;left:100px;width:1000px;text-align:center}
.reason h3{font-size:29px;font-weight:500;margin-bottom:6px}
.reason p{font-size:22px;font-style:italic;line-height:31.3px;color:#222}

/* clients */
.clients{position:absolute;left:0;top:2392px;width:1200px;height:470px;background:var(--royal)}
.clients-title{position:absolute;left:0;top:2410px;width:1200px;text-align:center;font-size:50px;font-weight:700;color:var(--white)}
.client-card{position:absolute;left:78px;top:2498px;width:1039px;height:304px;background:var(--white);border-radius:30px}
.client{position:absolute;display:flex;align-items:center;gap:10px;font-size:22px;font-weight:500;color:#333;transform:translateX(-50%)}
.client i{display:block;width:22px;height:22px;border-radius:50%;background:#333}
.slider-dots{position:absolute;left:0;top:2772px;width:1200px;text-align:center;font-size:14px;letter-spacing:3px;color:#222}

/* testimonials */
.quotes-title{position:absolute;left:0;top:2930px;width:1200px;text-align:center;font-size:52px;font-weight:700}
.underline{position:absolute;left:522px;top:3008px;width:156px;height:7px;background:var(--orange);border-radius:2px}
.quote{position:absolute;left:110px;width:980px;text-align:center;font-size:21px;font-style:italic;line-height:25px;color:var(--muted)}
.quote .who{margin-top:27px}
.quote-box{position:absolute;left:78px;width:1042px;background:var(--royal);border-radius:30px;color:var(--white);text-align:center;font-size:21px;font-style:italic;line-height:25px;padding:0 40px;display:flex;flex-direction:column;justify-content:center}
.quote-box .who{margin-top:25px}

/* footer */
.site-footer{position:absolute;left:0;top:3988px;width:1200px;height:147px;background:var(--white);box-shadow:0 -3px 8px rgba(0,0,0,.06)}
.footer-nav{position:absolute;left:365px;top:38px;display:flex;gap:44px;font-size:22px;font-weight:500}
.copyright{position:absolute;left:0;top:96px;width:1200px;text-align:center;font-size:14px}
</style>
</head>
<body>

<header class="site-header">
  <div class="brand">Brivane</div>
  <nav class="main-nav"><span>About</span><span>Services</span><span>Industries</span><span>Portfolio</span><span>Clients</span><span>Contact</span></nav>
</header>

<section class="hero">
  <h1 class="hero-title">Your voice, My<br>words.</h1>
  <p class="hero-sub">Copywriting and executive ghostwriting that speaks for your vision and your technology.</p>
  <div class="hero-photo" role="img" aria-label="Photo of Martin Olafsky standing in a light blue shirt and jeans"></div>
</section>
<a class="btn btn-primary" style="left:82px;top:525px;width:125px;height:48px">Contact Us</a>
<a class="btn btn-outline" style="left:232px;top:525px;width:125px;height:48px">Our Service</a>

<section>
  <div class="about-panel"></div>
  <div class="portrait" role="img" aria-label="Circular portrait of Martin Olafsky"></div>
  <h2 class="about-title">What I do ?</h2>
  <p class="about-text">Brivane Communications is a specialized copywriting agency led by an experienced award-winning novelist and executive ghostwriter. With a focus on the technology sector, the team has served clients in Israel, Europe, and the US for nearly three decades. Their articles can be found in leading publications, showcasing their industry expertise. As a boutique agency, Brivane Communications offers a unique and exclusive approach to copywriting, delivering high-quality content to meet clients' needs.</p>
  <a class="btn btn-accent" style="left:616px;top:1252px;width:151px;height:57px;font-size:17px">Our Service</a>
</section>

<section>
  <h2 class="why-title">Why choose me</h2>
  <div class="reason" style="top:1515px">
    <h3>My experience ;</h3>
    <p>"With almost 30 years in the tech industry, he possesses a thorough understanding of the field's language and jargon. This expertise enables him to craft persuasive content that resonates with the target audience and highlights a client's offerings."</p>
  </div>
  <div class="reason" style="top:1718px">
    <h3>My accomplishments ;</h3>
    <p>"As an award-winning novelist and regular contributor to top technology publications like Pulsar, ByteHarbor, and CapitalDrift, he has a proven talent for crafting compelling and informative content that resonates with readers. His impressive track record may attract potential clients looking to work with a skilled and successful writer."</p>
  </div>
  <div class="reason" style="top:1936px">
    <h3>Exclusive boutique agency ;</h3>
    <p>"Described as an 'exclusive boutique copywriting agency,' Brivane Communications offers a personalized and attentive service, setting itself apart from larger, generalized agencies. Potential clients may prefer the idea of working with a smaller team that can provide exceptional care and attention to detail."</p>
  </div>
  <div class="reason" style="top:2169px">
    <h3>Executive ghostwriting ;</h3>
    <p>"Described as an 'accomplished executive ghostwriter,' he has a proven ability to write on behalf of high-level executives and capture their voice and perspective. This skill is valuable to clients seeking to communicate complex ideas in a professional yet relatable manner."</p>
  </div>
</section>

<section>
  <div class="clients"></div>
  <h2 class="clients-title">Meet some of our clients...</h2>
  <div class="client-card"></div>
  <div class="client" style="left:300px;top:2563px"><i></i>Veltrona</div>
  <div class="client" style="left:588px;top:2563px"><i></i>Quillmark</div>
  <div class="client" style="left:892px;top:2563px"><i></i>Nuvio</div>
  <div class="client" style="left:250px;top:2683px"><i></i>Stratabyte</div>
  <div class="client" style="left:585px;top:2683px"><i></i>Orbelle</div>
  <div class="client" style="left:918px;top:2683px"><i></i>Kinetra Motion</div>
  <div class="slider-dots">•••••</div>
</section>

<section>
  <h2 class="quotes-title">What they’re saying</h2>
  <div class="underline"></div>
  <div class="quote" style="top:3068px">
    <p>“Martin has rich experience in the security arena, and a unique ability to get up to speed quickly on new material. He has produced excellent collateral for us over the past three years, and I highly recommend him to other security companies.”</p>
    <p class="who">Ravi Tomlen, CEO, Harborline Security</p>
  </div>
  <div class="quote-box" style="top:3225px;height:175px">
    <p>“Martin is a terrific resource for our company. A self-starter, who has generated a great deal of revenue for us and does high-quality work. Highly recommended.”</p>
    <p class="who">Glen Adair, Meridian Supply LLC</p>
  </div>
  <div class="quote" style="top:3459px">
    <p>“Martin is quick to understand new products and is able to take that knowledge and deliver very good results. He is creative, has a unique way with words, honest and easy to work with. I warmly recommend Martin to any business that wants to do justice to their marketing collateral.”</p>
    <p class="who">Lena Varga, Sr. Product Marketing Manager, Tidewell</p>
  </div>
  <div class="quote-box" style="top:3630px;height:213px">
    <p>“We've continued to work Martin over the years because he excels at turning ideas into viable and compelling marketing content that really reaches our target audience. His experience in the security field has also been a big plus for Shieldrun, and has enabled him to add real value to our company.”</p>
    <p class="who">Noa Kestel, Director of Marketing,Shieldrun (Vantara)</p>
  </div>
  <a class="btn btn-accent" style="left:532px;top:3868px;width:134px;height:50px;font-size:14px">Read More</a>
</section>

<footer class="site-footer">
  <nav class="footer-nav"><span>About</span><span>Services</span><span>Portfolio</span><span>Contact</span></nav>
  <p class="copyright">Copyright © 2023 Brivane Communications</p>
</footer>

</body>
</html>
```